New home maintenance business, on the back of business card i would like dot points of my services provided.
these include,
General household repairs and maintenance
Painting
Plankor/Plaster Repairs
Fencing
Gardening and landscaping
Cleaning and removals
Doors and windows
Hinges and Locks
Fly screen/ screen door Repairs
I like black,silver, red but ill leav it up to you guys as something may be better for business.. , would also it be possible to create a logo for me incorporating the K&T as i want to make up t shirts in future thankyou
Updates
i would also like to put Marco Tessani on the cards aswell please, and on back change painter to proffesional painter and decorator, please
i like alot of the designs sofar, i cant put my finger on wat 1 yet though!! cheers guys
Industry/Entity Type
Business
Contact Information for Business Card
K&T HOME MAINTENANCE SERVICES
Lenny Tessani 0498127654
ktmaintenance@mailvexa.com
ABN:71452038619
Look and feel
Each slider illustrates characteristics of the customer's brand and the style your logo design should communicate.

```html
<!DOCTYPE html>
<html lang="en">
<head>
<meta charset="utf-8">
<title>K&amp;T Home Maintenance Services – Business Card</title>
<link rel="stylesheet" href="https://fonts.googleapis.com/css2?family=Mulish:wght@400;700;800&display=swap">
<style>
  :root {
    --backdrop: #e9e9ee;
    --card-dark: #3a3a3c;
    --card-light: #ffffff;
    --brand-red: #c1262b;
    --text-light: #f2f2f2;
    --text-grey: #66605c;
    --shadow: rgba(0, 0, 0, 0.18);
  }
  * { box-sizing: border-box; margin: 0; padding: 0; }
  html, body {
    width: 1200px;
    height: 934px;
    overflow: hidden;
    background: var(--backdrop);
    font-family: "Mulish", "Century Gothic", sans-serif;
  }
  .sheet {
    width: 1200px;
    height: 934px;
    display: flex;
    align-items: center;
    justify-content: center;
    gap: 40px;
  }
  .card {
    position: relative;
    width: 540px;
    height: 330px;
    box-shadow: 0 6px 18px var(--shadow);
    overflow: hidden;
  }
  .card--back { background: var(--card-dark); }
  .card--front { background: var(--card-light); }

  /* Brand lock-up: plain square + name between two rules */
  .brand {
    position: absolute;
    display: flex;
    align-items: center;
    gap: 10px;
  }
  .card--back .brand { top: 40px; right: 34px; }
  .card--front .brand { top: 70px; right: 40px; }
  .brand__mark {
    width: 48px;
    height: 48px;
    background: var(--brand-red);
    flex: none;
  }
  .brand__name {
    border-top: 2px solid var(--brand-red);
    border-bottom: 2px solid var(--brand-red);
    padding: 6px 4px 6px 2px;
    font-weight: 800;
    font-size: 18px;
    letter-spacing: 0.2px;
    white-space: nowrap;
    line-height: 22px;
  }
  .card--back .brand__name { color: var(--text-light); }
  .card--front .brand__name { color: var(--text-grey); }

  .service-list {
    position: absolute;
    right: 34px;
    bottom: 38px;
    text-align: right;
    list-style: none;
    color: var(--text-light);
    font-size: 11.5px;
    line-height: 19px;
    letter-spacing: 0.6px;
    text-transform: uppercase;
  }
  .service-list .accent { color: var(--brand-red); }

  .contact {
    position: absolute;
    left: 44px;
    bottom: 34px;
    color: var(--text-grey);
    font-size: 13px;
    line-height: 18px;
  }
  .contact__names { margin-bottom: 4px; }
  .contact__name {
    color: var(--brand-red);
    font-weight: 800;
    font-size: 16px;
    line-height: 21px;
    letter-spacing: 0.5px;
  }
  .contact__label { font-weight: 700; }
</style>
</head>
<body>
<main class="sheet">
  <section class="card card--back" aria-label="Business card back">
    <div class="brand">
      <span class="brand__mark" aria-hidden="true"></span>
      <span class="brand__name">K&amp;T HOME MAINTENANCE SERVICES</span>
    </div>
    <ul class="service-list">
      <li>General household repairs and maintenance</li>
      <li><span class="accent">Professional painter and decorator</span> · Fencing</li>
      <li>Plankor / Plaster repairs · <span class="accent">Gardening and landscaping</span></li>
      <li><span class="accent">Cleaning and removals</span> · Doors and windows · <span class="accent">Hinges and locks</span></li>
      <li>Fly screen / Screen door repairs</li>
    </ul>
  </section>

  <section class="card card--front" aria-label="Business card front">
    <div class="brand">
      <span class="brand__mark" aria-hidden="true"></span>
      <span class="brand__name">K&amp;T HOME MAINTENANCE SERVICES</span>
    </div>
    <div class="contact">
      <div class="contact__names">
        <p class="contact__name">LENNY TESSANI</p>
        <p class="contact__name">MARCO TESSANI</p>
      </div>
      <p><span class="contact__label">Phone:</span> 0498127654</p>
      <p><span class="contact__label">Email:</span> ktmaintenance@mailvexa.com</p>
      <p><span class="contact__label">ABN:</span> 71452038619</p>
    </div>
  </section>
</main>
</body>
</html>
```